Harmony Swift Care Business card

We want a business card that matches our business theme. Our website is www.swiftcarehub.example
The company name is Harmony Swift Care
The persons having the business cards will be doctors
My logo is attached.
We have a drive-thru medical center where our motto is Fast, Reliable, and Convenient. Our goal is to change the medical space while utilizing technologies, keeping a professional and clean look

Medical

Info on the card should be: Name, Position, Cell number, website, email address, possibly the office line as well

Requirements
Must have
• Logo
Nice to have
• Professional medical feel with our logo colors incorporated

```html
<!DOCTYPE html>
<html lang="en">
<head>
<meta charset="utf-8">
<title>Harmony Swift Care – Business Card</title>
<link rel="stylesheet" href="https://fonts.googleapis.com/css2?family=Montserrat:wght@400;500;600;800&display=swap">
<style>
  :root {
    --navy: #1b3f9a;
    --navy-deep: #173687;
    --sky: #3dbdf0;
    --white: #ffffff;
    --backdrop: #3a3b3e;
  }
  * { margin: 0; padding: 0; box-sizing: border-box; }
  html, body { width: 1200px; height: 801px; overflow: hidden; }
  body {
    background: var(--backdrop);
    font-family: "Montserrat", sans-serif;
    display: flex;
    align-items: center;
    justify-content: center;
    gap: 40px;
  }
  .card {
    position: relative;
    width: 540px;
    height: 309px;
    border-radius: 16px;
    overflow: hidden;
  }
  /* Back side */
  .card-back { background: var(--navy); }
  .card-back .back-field {
    position: absolute; inset: 0;
    background: radial-gradient(circle at 70% 30%, #2550b0 0%, var(--navy) 55%, var(--navy-deep) 100%);
  }
  .card-back .back-brand {
    position: absolute; inset: 0;
    display: flex; align-items: center; justify-content: center; gap: 12px;
    color: var(--sky); font-weight: 800; font-size: 22px;
  }
  .brand-dot {
    width: 30px; height: 30px; border-radius: 50%;
    border: 4px solid var(--sky);
  }
  /* Front side */
  .card-front { background: var(--white); }
  .front-wave { position: absolute; inset: 0; }
  .front-brand {
    position: absolute; top: 20px; right: 30px;
    text-align: right; color: var(--navy);
  }
  .front-brand .brand-row {
    display: flex; align-items: center; justify-content: flex-end; gap: 10px;
    font-weight: 800; font-size: 22px;
  }
  .front-brand .brand-dot { border-color: var(--navy); width: 32px; height: 32px; }
  .tagline {
    margin-top: 4px; font-size: 10px; font-weight: 600; letter-spacing: 0.4px;
  }
  .addresses {
    position: absolute; right: 30px; top: 150px;
    text-align: right; color: var(--white);
    font-size: 12px; line-height: 1.55; font-weight: 500;
  }
  .person {
    position: absolute; left: 30px; bottom: 20px; color: var(--white);
  }
  .person-name { color: var(--sky); font-weight: 800; font-size: 26px; line-height: 1; }
  .person-role { font-size: 13px; font-weight: 500; margin-top: 4px; }
  .person-rule { width: 175px; height: 1.5px; background: var(--sky); margin: 8px 0 10px; }
  .contact-list { list-style: none; font-size: 13px; line-height: 1.55; }
  .contact-list li { display: flex; align-items: center; gap: 8px; }
  .contact-list svg { width: 12px; height: 12px; flex: none; }
</style>
</head>
<body>

<div class="card card-back">
  <div class="back-field" role="img" aria-label="Faint repeating brand-mark pattern on deep blue"></div>
  <div class="back-brand"><span class="brand-dot"></span><span>Harmony Swift Care</span></div>
</div>

<div class="card card-front">
  <svg class="front-wave" viewBox="0 0 540 309" preserveAspectRatio="none" aria-hidden="true">
    <path d="M0,138 C140,108 300,128 420,106 C490,93 530,78 540,56 L540,70 C530,90 490,105 420,118 C300,140 140,120 0,150 Z" fill="var(--sky)"/>
    <path d="M0,150 C140,120 300,140 420,118 C490,105 530,90 540,70 L540,309 L0,309 Z" fill="var(--navy)"/>
  </svg>

  <div class="front-brand">
    <div class="brand-row"><span>Harmony Swift Care</span><span class="brand-dot"></span></div>
    <div class="tagline">FAST | RELIABLE | CONVENIENT</div>
  </div>

  <div class="addresses">
    42 Lantern Road, Eastfield<br>
    7 Harbor Lane, Upper Road<br>
    Bayview
  </div>

  <div class="person">
    <div class="person-name">Marisol K.</div>
    <div class="person-role">Assistant Manager</div>
    <div class="person-rule"></div>
    <ul class="contact-list">
      <li><svg viewBox="0 0 12 12"><path d="M2.5 1 L4.5 1 L5 3.5 L3.8 4.5 C4.5 6 6 7.5 7.5 8.2 L8.5 7 L11 7.5 L11 9.5 C11 10.3 10.3 11 9.5 11 C5 11 1 7 1 2.5 C1 1.7 1.7 1 2.5 1 Z" fill="var(--sky)"/></svg>+1 (555) 014-2267</li>
      <li><svg viewBox="0 0 12 12"><rect x="0.5" y="2" width="11" height="8" rx="1" fill="var(--sky)"/><path d="M1 2.5 L6 6.5 L11 2.5" stroke="var(--navy)" fill="none"/></svg>info@swiftcarehub.example</li>
      <li><svg viewBox="0 0 12 12"><circle cx="6" cy="6" r="5.5" fill="var(--sky)"/><path d="M0.5 6 H11.5 M6 0.5 C3.5 3 3.5 9 6 11.5 M6 0.5 C8.5 3 8.5 9 6 11.5" stroke="var(--navy)" stroke-width="0.8" fill="none"/></svg>www.swiftcarehub.example</li>
    </ul>
  </div>
</div>

</body>
</html>
```